Design for Chirpwall Ad to promote Laptops purchase

Need a graphic design for a Chirpwall Ad - to promote 2 laptops (PC and Zorvane) with the stated required ad-text.

AD TEXT:

FOR SME BUSINESS ONLY!
Chat with us!
To get advice on how to apply
and defray up to 80%* of business laptop purchase cost!

*Terms and Conditions apply

Image for reference only

Target Market(s)

Small medium business

Font styles to use
Sans Serif

Requirements
Must have
• 2 laptop images (see attached ) - 1 vector image of ZORVANE , and pls try to create another vector image of PC laptop (where screen is showing Blue Pendrel screen)

```html
<!DOCTYPE html>
<html lang="en">
<head>
<meta charset="utf-8">
<title>SME Business Laptop Advice</title>
<link href="https://fonts.googleapis.com/css2?family=Montserrat:ital,wght@0,400;0,700;0,800;0,900;1,700&display=swap" rel="stylesheet">
<style>
  :root {
    --ink: #1a1a1a;
    --ribbon: #e31e25;
    --ribbon-dark: #a8141a;
    --teal: #38c0a8;
    --yellow: #f2d52a;
    --yellow-deep: #e8b318;
    --silver-light: #ffffff;
    --silver-mid: #d9d9d9;
    --screen-deep: #0b5fb8;
    --screen-bright: #2fb5ee;
    --body-silver: #c4c6c9;
    --white: #ffffff;
  }
  * { margin: 0; padding: 0; box-sizing: border-box; }
  html, body { width: 1200px; height: 1200px; overflow: hidden; }
  body { font-family: "Montserrat", Arial, sans-serif; color: var(--ink); }
  .ad {
    position: relative; width: 1200px; height: 1200px; overflow: hidden;
    background: radial-gradient(ellipse at 55% 35%, #f4f4f4 0%, #e2e2e2 55%, #d4d4d4 100%);
  }
  .layer { position: absolute; left: 0; top: 0; width: 1200px; height: 1200px; }
  .headline {
    position: absolute; left: 200px; top: 118px; width: 798px; height: 88px;
    display: flex; align-items: center; justify-content: center;
    color: var(--white); font-weight: 800; font-size: 54px; letter-spacing: -0.5px;
  }
  .offer {
    position: absolute; left: 0; top: 260px; width: 1200px; text-align: center;
    font-weight: 400; font-size: 38px; line-height: 46px; letter-spacing: 0.5px;
  }
  .offer strong { font-weight: 800; }
  .offer .offer-emphasis { display: block; font-weight: 800; font-size: 49px; line-height: 58px; margin-top: -2px; }
  .laptop { position: absolute; }
  .laptop-pc {
    left: 600px; top: 462px; width: 564px; height: 386px; border-radius: 10px;
    background: linear-gradient(to bottom, #1f8fdc 0%, var(--screen-bright) 52%, #b9bbbe 62%, #dfe0e2 100%);
  }
  .laptop-zorvane {
    left: 42px; top: 478px; width: 728px; height: 418px; border-radius: 14px 14px 8px 8px;
    background: linear-gradient(to bottom, #1268c4 0%, var(--screen-bright) 60%, #1279d0 88%, #d6d7d9 92%, #f2f2f2 96%, #a8aaac 100%);
  }
  .cta {
    position: absolute; right: 48px; top: 1024px;
    font-weight: 800; font-size: 63px; letter-spacing: -1.5px; line-height: 1;
  }
  .terms {
    position: absolute; right: 46px; top: 1136px;
    font-weight: 700; font-style: italic; font-size: 17px;
  }
</style>
</head>
<body>
<div class="ad">
  <svg class="layer waves" viewBox="0 0 1200 1200" aria-hidden="true">
    <defs>
      <linearGradient id="silverBand" x1="0" y1="0" x2="1" y2="1">
        <stop offset="0" stop-color="var(--silver-light)"/>
        <stop offset="1" stop-color="var(--silver-mid)"/>
      </linearGradient>
    </defs>
    <path class="wave-teal" fill="var(--teal)" d="M0,860 C300,860 650,760 1200,660 L1200,780 C800,840 420,930 0,1000 Z"/>
    <path class="wave-yellow" fill="var(--yellow)" d="M0,1000 C420,930 800,840 1200,780 L1200,1200 L0,1200 Z"/>
    <path class="wave-teal-lower" fill="var(--teal)" d="M0,930 C250,960 420,900 700,880 C500,910 300,1000 0,1080 Z"/>
    <path class="wave-silver" fill="url(#silverBand)" d="M0,990 C250,990 470,910 720,885 C480,950 320,1070 160,1200 L0,1200 Z"/>
    <path class="wave-yellow-edge" fill="#efe07a" d="M0,1100 C60,1140 90,1170 120,1200 L0,1200 Z"/>
    <rect class="footer-band" x="448" y="1124" width="752" height="44" fill="var(--yellow-deep)"/>
  </svg>

  <svg class="layer ribbon" viewBox="0 0 1200 1200" aria-hidden="true">
    <polygon fill="var(--ribbon)" points="134,146 242,146 242,234 134,234 162,190"/>
    <polygon fill="var(--ribbon-dark)" points="200,206 242,206 242,234"/>
    <polygon fill="var(--ribbon)" points="958,146 1066,146 1038,190 1066,234 958,234"/>
    <polygon fill="var(--ribbon-dark)" points="998,206 958,206 958,234"/>
    <rect fill="var(--ribbon)" x="200" y="118" width="798" height="88"/>
  </svg>
  <div class="headline">FOR SME BUSINESS ONLY!</div>

  <p class="offer">
    TO GET ADVICE ON HOW TO APPLY<br>
    AND DEFRAY <strong>UP TO 80%*</strong> OF BUSINESS
    <span class="offer-emphasis">LAPTOP PURCHASE COST!</span>
  </p>

  <div class="laptop laptop-pc" role="img" aria-label="Silver PC laptop, open at an angle with keyboard visible, screen showing a blue Pendrel desktop"></div>
  <div class="laptop laptop-zorvane" role="img" aria-label="Silver Zorvane laptop seen from the front, black bezel and blue wallpaper screen on a thin silver base"></div>

  <svg class="layer chat-icon" viewBox="0 0 1200 1200" aria-hidden="true">
    <path fill="#3a3a3a" d="M988,920 H1054 Q1074,920 1074,940 V966 Q1074,986 1054,986 H1004 L986,1002 L990,986 Q968,984 968,964 V940 Q968,920 988,920 Z"/>
    <path fill="var(--ribbon)" d="M1036,936 H1128 Q1148,936 1148,956 V1000 Q1148,1016 1132,1018 L1128,1036 L1110,1018 H1036 Q1016,1018 1016,998 V956 Q1016,936 1036,936 Z"/>
    <circle fill="var(--yellow)" cx="1060" cy="973" r="8"/>
    <circle fill="var(--yellow)" cx="1084" cy="973" r="8"/>
    <circle fill="var(--yellow)" cx="1108" cy="973" r="8"/>
  </svg>
  <div class="cta">CHAT WITH US!</div>
  <div class="terms">*Terms and Conditions apply</div>
</div>
</body>
</html>
```